Velune gifts app, mini-website

We have designed and launched an app to sell gift cards (a card with monetary value) and greeting cards (think pinwheel paper cards made digital).

Target Market(s)

anyone who would buy and send gift cards via an app

Coding

Coded - Design and coding required

Number of Pages Required

1 page

```html
<!DOCTYPE html>
<html lang="en">
<head>
<meta charset="utf-8">
<title>Velune Gifts – Buy and send gift cards via an app</title>
<link rel="stylesheet" href="https://fonts.googleapis.com/css2?family=Lexend:wght@400;500;600&family=Arimo:wght@400;500;700&display=swap">
<style>
:root{
  --red:#b02226;
  --red-dark:#9c1c20;
  --ink:#222222;
  --text:#3a3a3a;
  --muted:#7b7b7b;
  --blush:#f6e3e3;
  --paper:#ffffff;
  --mist:#f5f5f5;
  --card:#f8f8f8;
  --star:#f7941d;
  --pill:#2f6fe4;
}
*{box-sizing:border-box;margin:0;padding:0}
html,body{width:1200px;height:3830px;overflow:hidden}
body{position:relative;background:var(--paper);font-family:"Arimo",Arial,sans-serif;color:var(--text)}
.abs{position:absolute}
h1,h2,h3{font-family:"Lexend",Arial,sans-serif;font-weight:500;color:var(--ink)}

/* header */
.site-header{position:absolute;left:0;top:0;width:1200px;height:92px;background:var(--paper)}
.brand{position:absolute;left:127px;top:34px;display:flex;align-items:center;gap:8px;font-family:"Lexend",sans-serif;font-weight:600;font-size:22px;color:var(--red)}
.brand-mark{width:22px;height:22px;background:var(--red);border-radius:4px}
.main-nav a{position:absolute;top:36px;font-family:"Lexend",sans-serif;font-size:18px;color:var(--ink);text-decoration:none}
.fav-btn{position:absolute;left:871px;top:29px;width:38px;height:40px;border-radius:10px;background:var(--red);display:flex;align-items:center;justify-content:center}
.dl-btn{position:absolute;left:919px;top:28px;width:152px;height:42px;border-radius:21px;background:#333;color:#fff;font-family:"Lexend",sans-serif;font-size:15px;display:flex;align-items:center;justify-content:center}

/* hero */
.hero{position:absolute;left:0;top:92px;width:1200px;height:508px;background:var(--red)}
.hero h1{position:absolute;left:127px;top:138px;font-size:53px;line-height:56px;color:#fff}
.hero .outline-btn{position:absolute;left:127px;top:280px;width:228px;height:50px}
.outline-btn{border:2px solid #fff;border-radius:26px;color:#fff;font-family:"Lexend",sans-serif;font-size:20px;display:flex;align-items:center;justify-content:center}
.hero-art{position:absolute;left:700px;top:36px;width:356px;height:472px;border-radius:170px 170px 10px 10px;background:radial-gradient(circle at 50% 30%,#f3a0c8 0%,#8fb8f0 30%,#f2c84a 55%,#e0475c 80%,rgba(176,34,38,0) 100%);opacity:.9}

/* phone */
.phone{position:absolute;background:#fff;border:4px solid #111;border-radius:30px;overflow:hidden;font-family:"Arimo",sans-serif;color:#111}
.phone::before{content:"";position:absolute;left:50%;top:0;transform:translateX(-50%);width:32%;height:8px;background:#111;border-radius:0 0 8px 8px}
.time-pill{position:absolute;background:var(--pill);color:#fff;border-radius:8px;font-size:9px;padding:1px 8px}
.mini-brand{position:absolute;left:0;width:100%;display:flex;justify-content:center;align-items:center;gap:4px;font-family:"Lexend",sans-serif;font-weight:600;font-size:11px;color:var(--red)}
.mini-brand::before{content:"";width:9px;height:9px;background:var(--red);border-radius:2px}

/* intro */
.intro-blob{position:absolute;left:119px;top:800px;width:420px;height:380px;background:var(--blush);border-radius:55% 45% 50% 50%/40% 45% 55% 60%}
.intro-phone{left:242px;top:735px;width:252px;height:499px}
.steps{position:absolute;left:0;top:84px;width:100%;display:flex;justify-content:space-between;padding:0 12px;font-size:8px;font-weight:700;text-align:center}
.step-dot{display:block;margin:0 auto 3px;width:11px;height:11px;border-radius:50%;font-size:7px;line-height:11px;color:#111}
.step-dot.on{background:var(--red);color:#fff}
.phone-rule{position:absolute;left:0;width:100%;height:1px;background:#ddd}
.field{position:absolute;left:16px;width:216px;border-bottom:1px solid #cfcfcf;padding-bottom:5px}
.field small{display:block;font-size:6.5px;color:#888;margin-bottom:7px}
.field span{font-size:9.5px}
.phone-cta{position:absolute;background:#222;color:#fff;border-radius:16px;font-size:10px;display:flex;align-items:center;justify-content:center}
.ph-art{position:absolute;border-radius:14px;background:linear-gradient(160deg,#9cc8f2,#f19bbf 45%,#f4c94d 75%,#d9404f)}

.intro-copy{position:absolute;left:590px;top:800px;width:420px}
.intro-copy h2{font-size:38px;line-height:44px;font-weight:500}
.intro-copy p{margin-top:30px;font-size:15px;line-height:18px;color:#444}
.intro-copy .lead{margin-top:30px;font-size:18px;color:#222}

/* store badges */
.store{position:absolute;width:164px;height:47px;background:#000;border-radius:6px;color:#fff;display:flex;align-items:center;gap:10px;padding-left:14px;border:1px solid #555}
.store i{width:22px;height:22px;border-radius:50%;background:#fff;flex:none}
.store small{display:block;font-size:9px;letter-spacing:.3px;line-height:10px}
.store b{display:block;font-size:20px;font-weight:500;line-height:22px}

/* features */
.section-title{position:absolute;left:0;width:1200px;text-align:center}
.features-title{top:1406px;font-size:38px}
.features-sub{position:absolute;left:320px;top:1469px;width:560px;text-align:center;font-size:14.5px;line-height:18px;color:#333}
.feature-card{position:absolute;top:1542px;width:294px;height:302px;background:#fff;border-radius:18px;box-shadow:0 10px 30px rgba(0,0,0,.07);text-align:center}
.feature-card svg{position:absolute;left:50%;top:42px;transform:translateX(-50%)}
.feature-card h3{position:absolute;top:116px;width:100%;font-size:20px;line-height:23px;font-weight:400;color:#222}
.feature-card h3 em{font-style:normal;color:var(--red)}
.feature-card p{position:absolute;left:28px;top:180px;width:238px;font-size:14.5px;line-height:18px;color:#808080}

/* showcase */
.side-blob{position:absolute;left:950px;top:1948px;width:420px;height:760px;background:#fcf0f0;border-radius:60% 0 0 50%}
.showcase-title{top:2088px;font-size:36px}
.show-phone{text-align:center;box-shadow:0 12px 30px rgba(0,0,0,.12)}
.show-phone .howto{position:absolute;width:100%;font-size:6.5px;color:#444}
.show-phone .ttl{position:absolute;width:100%;font-family:"Arimo",sans-serif;font-weight:700;color:#111}
.show-phone .cap{position:absolute;left:10%;width:80%;font-size:7px;line-height:9px;color:#555}
.dots{position:absolute;left:0;width:100%;display:flex;justify-content:center;gap:4px}
.dots span{width:4px;height:4px;border-radius:2px;background:#bbb}
.dots span.on{width:10px;background:#111}
.skip{position:absolute;width:100%;font-size:8px}

/* reviews */
.reviews-title{top:2808px;font-size:50px}
.review{position:absolute;top:2900px;width:297px;height:203px;background:var(--card);border-radius:10px;padding:20px 24px}
.review .stars{color:var(--star);font-size:25px;letter-spacing:1px;line-height:25px}
.review h4{margin-top:10px;font-size:16px;font-weight:500;color:#444}
.review p{margin-top:18px;font-size:14.5px;line-height:18px;color:#888}
.review-dots{position:absolute;left:567px;top:3128px;display:flex;gap:6px}
.review-dots span{width:8px;height:8px;border-radius:50%;background:#999}

/* cta */
.cta{position:absolute;left:0;top:3225px;width:1200px;height:317px;background:var(--red)}
.cta-art{position:absolute;left:119px;top:30px;width:275px;height:270px;border-radius:120px 120px 20px 20px;background:radial-gradient(circle at 50% 55%,#f7c843 0%,#e34b4b 45%,#6aa84f 70%,#f4a9a9 85%,rgba(240,170,170,0) 100%)}
.cta h2{position:absolute;left:445px;top:90px;width:620px;font-size:33px;line-height:38px;color:#fff}
.cta .outline-btn{position:absolute;left:445px;top:180px;width:211px;height:57px}

/* footer */
.site-footer{position:absolute;left:0;top:3542px;width:1200px;height:288px;background:var(--mist)}
.site-footer .label{position:absolute;font-family:"Lexend",sans-serif;font-size:14px;color:#111}
.social{position:absolute;top:82px;width:38px;height:38px;border-radius:50%}
.footer-rule{position:absolute;left:128px;top:161px;width:943px;height:1px;background:#dcdcdc}
.copyright{position:absolute;left:0;top:210px;width:1200px;text-align:center;font-size:14px;color:#222}
</style>
</head>
<body>

<header class="site-header">
  <div class="brand"><span class="brand-mark"></span>Velune</div>
  <nav class="main-nav">
    <a style="left:510px">Home</a>
    <a style="left:602px">How it Works</a>
    <a style="left:767px">App</a>
  </nav>
  <div class="fav-btn"><svg width="16" height="15" viewBox="0 0 24 22"><path d="M12 21 2.5 11.5A5.5 5.5 0 0 1 12 4a5.5 5.5 0 0 1 9.5 7.5Z" fill="#fff"/></svg></div>
  <div class="dl-btn">Download App</div>
</header>

<section class="hero">
  <h1>Feeling grateful<br>for someone?</h1>
  <div class="outline-btn">Download The App</div>
  <div class="hero-art" role="img" aria-label="Illustration of colourful balloons tied to stacked wrapped gift boxes"></div>
</section>

<section class="intro">
  <div class="intro-blob"></div>
  <div class="phone intro-phone">
    <span class="time-pill" style="left:24px;top:10px">9:28</span>
    <svg class="abs" style="left:22px;top:55px" width="12" height="10"><path d="M0 1h12M0 5h12M0 9h12" stroke="#333" stroke-width="1.5"/></svg>
    <div class="mini-brand" style="top:52px">Velune</div>
    <svg class="abs" style="left:208px;top:52px" width="14" height="13"><path d="M1 1h2l2 8h7l1-6H4" fill="none" stroke="#333" stroke-width="1.3"/></svg>
    <div class="steps">
      <div><span class="step-dot on">1</span>Recipient</div>
      <div><span class="step-dot">2</span>Greeting Card</div>
      <div><span class="step-dot">3</span>Gift Cards</div>
    </div>
    <div class="phone-rule" style="top:116px"></div>
    <div class="abs" style="left:6px;top:162px;font-family:Lexend,sans-serif;font-weight:600;font-size:21px;line-height:22px">Feeling<br>grateful for<br>someone?</div>
    <div class="ph-art" style="left:148px;top:135px;width:84px;height:124px" role="img" aria-label="Balloons over gift boxes"></div>
    <div class="abs" style="left:16px;top:276px;width:190px;font-size:8.5px;line-height:11px;color:#555">Enter your recipient information to send your perfect digital gift</div>
    <div class="field" style="top:306px"><small>Name of Recipient</small><span>Tomas</span></div>
    <div class="field" style="top:348px"><small>Email of Recipient (optional)</small><span>tomas@mailnest.test</span></div>
    <div class="field" style="top:391px"><small>Country</small><span>Canada</span>
      <svg class="abs" style="right:4px;top:22px" width="10" height="6"><path d="M0 0h10L5 6Z" fill="#222"/></svg></div>
    <div class="phone-cta" style="left:14px;top:455px;width:216px;height:30px">Continue</div>
  </div>

  <div class="intro-copy">
    <h2>Buy and send gift<br>cards via an app</h2>
    <p>Lorem ipsum dolor sit amet, consectetur adipiscing elit, sed do eiusmod tempor incididunt ut labore et dolore magna aliqua. Quis ipsum suspendisse ultrices gravida. Risus commodo viverra maecenas accumsan lacus vel facilisis.</p>
    <div class="lead">Download the latest version of the app from</div>
  </div>
  <div class="store" style="left:593px;top:1072px"><i></i><div><small>GET IT ON</small><b>PlayHub</b></div></div>
  <div class="store" style="left:766px;top:1072px"><i></i><div><small>Download on the</small><b>AppVault</b></div></div>
</section>

<section class="features">
  <h2 class="section-title features-title">Discover the Features</h2>
  <p class="features-sub">Lorem ipsum dolor sit amet, consectetur adipiscing elit, sed do eiusmod tempor incididunt ut labore et dolore magna aliqu suspeultrices gravida.</p>

  <article class="feature-card" style="left:128px">
    <svg width="50" height="40" viewBox="0 0 50 40"><circle cx="25" cy="9" r="7" fill="var(--red)"/><circle cx="10" cy="12" r="5" fill="var(--red)"/><circle cx="40" cy="12" r="5" fill="var(--red)"/><path d="M12 38a13 13 0 0 1 26 0Z" fill="var(--red)"/><path d="M0 34a10 10 0 0 1 16-8 16 16 0 0 0-5 8Z" fill="var(--red)"/><path d="M50 34a10 10 0 0 0-16-8 16 16 0 0 1 5 8Z" fill="var(--red)"/></svg>
    <h3>Organize<br>your <em>contacts</em></h3>
    <p>Lore magna aliquis ipsum suspe ndisse ultrices gravida. Risus com modo viverra maecenas accumsan lacus vel facmaecenilisis.</p>
  </article>
  <article class="feature-card" style="left:452px">
    <svg width="44" height="38" viewBox="0 0 44 38"><path d="M0 6 13 0v32L0 38Z" fill="var(--red)"/><path d="M15 0l14 6v32l-14-6Z" fill="var(--red)"/><path d="M31 6 44 0v32l-13 6Z" fill="var(--red)"/></svg>
    <h3>Map<br>your <em>contacts</em></h3>
    <p>Lore magna aliquis ipsum suspe ndisse ultrices gravida. Risus com modo viverra maecenas accumsan lacus vel facmaecenilisis.</p>
  </article>
  <article class="feature-card" style="left:776px">
    <svg width="40" height="40" viewBox="0 0 40 40"><rect x="2" y="12" width="36" height="8" fill="var(--red)"/><rect x="5" y="22" width="30" height="18" fill="var(--red)"/><rect x="18" y="12" width="4" height="28" fill="#fff"/><path d="M20 12c-4-10-14-8-10 0M20 12c4-10 14-8 10 0" fill="none" stroke="var(--red)" stroke-width="3"/></svg>
    <h3>Send <em>Gifts</em><br>your loved one</h3>
    <p>Lore magna aliquis ipsum suspe ndisse ultrices gravida. Risus com modo viverra maecenas accumsan lacus vel facmaecenilisis.</p>
  </article>

  <div class="store" style="left:431px;top:1905px"><i></i><div><small>GET IT ON</small><b>PlayHub</b></div></div>
  <div class="store" style="left:604px;top:1905px"><i></i><div><small>Download on the</small><b>AppVault</b></div></div>
</section>

<section class="showcase">
  <div class="side-blob"></div>
  <h2 class="section-title showcase-title">Our App Showcase</h2>

  <div class="phone show-phone" style="left:152px;top:2230px;width:132px;height:398px;z-index:1;border-radius:22px">
    <span class="time-pill" style="left:18px;top:8px">9:28</span>
    <svg class="abs" style="left:20px;top:44px" width="10" height="8"><path d="M0 1h10M0 4h10M0 7h10" stroke="#333"/></svg>
    <div class="mini-brand" style="top:40px;left:60px;width:auto;font-size:9px">Velune</div>
    <div class="abs" style="left:10px;top:72px;font-size:7px;font-weight:700">Recipient</div>
    <div class="abs" style="left:72px;top:72px;font-size:7px;font-weight:700">Greeting Card</div>
    <div class="abs" style="left:4px;top:130px;text-align:left;font-family:Lexend,sans-serif;font-weight:600;font-size:17px;line-height:17px">Feeling<br>grateful for<br>someone?</div>
    <div class="abs" style="left:10px;top:220px;width:110px;text-align:left;font-size:6.5px;line-height:8px;color:#555">Enter your recipient information to send your perfect digital gift</div>
    <div class="abs" style="left:10px;top:258px;font-size:7px">Tomas</div>
    <div class="abs" style="left:10px;top:296px;font-size:7px">tomas@mailnest.test</div>
    <div class="abs" style="left:10px;top:330px;font-size:7px">Canada</div>
    <div class="phone-cta" style="left:10px;top:360px;width:140px;height:20px;font-size:7px;padding-left:60px">Continue</div>
  </div>

  <div class="phone show-phone" style="left:273px;top:2205px;width:225px;height:444px;z-index:2">
    <div class="mini-brand" style="top:34px">Velune</div>
    <div class="howto" style="top:64px">How it works</div>
    <div class="ttl" style="top:80px;font-size:15px">Pick a recipient</div>
    <div class="ph-art" style="left:28px;top:120px;width:170px;height:170px" role="img" aria-label="Illustration of a phone showing a contact list beside gift boxes"></div>
    <div class="cap" style="top:308px">Tell us who should receive your digital gift</div>
    <div class="dots" style="top:334px"><span class="on"></span><span></span><span></span><span></span></div>
    <div class="phone-cta" style="left:10px;top:386px;width:196px;height:24px;font-size:8px">Next</div>
    <div class="skip" style="top:418px">Skip</div>
  </div>

  <div class="phone show-phone" style="left:474px;top:2174px;width:251px;height:498px;z-index:3">
    <span class="time-pill" style="left:34px;top:18px">9:27</span>
    <div class="mini-brand" style="top:66px">Velune</div>
    <div class="howto" style="top:98px">How it works</div>
    <div class="ttl" style="top:112px;font-size:16px">Pick a greeting card</div>
    <div class="ph-art" style="left:36px;top:160px;width:172px;height:170px" role="img" aria-label="Illustration of people choosing a greeting card among gifts"></div>
    <div class="cap" style="top:364px">Choose a greeting card and customize the message</div>
    <div class="dots" style="top:390px"><span></span><span class="on"></span><span></span><span></span></div>
    <div class="phone-cta" style="left:26px;top:424px;width:192px;height:27px;font-size:9px">Next</div>
    <div class="skip" style="top:460px">Skip</div>
  </div>

  <div class="phone show-phone" style="left:721px;top:2205px;width:190px;height:444px;z-index:2">
    <span class="time-pill" style="left:-6px;top:4px">9:27</span>
    <div class="mini-brand" style="top:46px">Velune</div>
    <div class="howto" style="top:76px">How it works</div>
    <div class="ttl" style="top:94px;font-size:14px">Add a gift card</div>
    <div class="ph-art" style="left:6px;top:130px;width:174px;height:150px" role="img" aria-label="Illustration of a storefront with gift bags and a buy sign"></div>
    <div class="cap" style="top:310px">Send a digital gift card they can spend at many retailers</div>
    <div class="dots" style="top:354px"><span></span><span></span><span class="on"></span><span></span></div>
    <div class="phone-cta" style="left:10px;top:388px;width:164px;height:22px;font-size:8px">Next</div>
    <div class="skip" style="top:418px">Skip</div>
  </div>

  <div class="phone show-phone" style="left:909px;top:2230px;width:143px;height:398px;z-index:1;border-radius:22px">
    <div class="mini-brand" style="top:40px;font-size:10px">Velune</div>
    <div class="howto" style="top:68px">How it works</div>
    <div class="ttl" style="top:82px;font-size:13px">Checkout</div>
    <div class="ph-art" style="left:4px;top:130px;width:120px;height:90px" role="img" aria-label="Illustration of a shopper pushing a cart full of gifts"></div>
    <div class="cap" style="top:276px;left:4px;width:126px">Review your order and select a delivery method for your digital gift</div>
    <div class="dots" style="top:312px"><span></span><span></span><span></span><span class="on"></span></div>
    <div class="phone-cta" style="left:4px;top:336px;width:126px;height:22px;font-size:7px">Get Started</div>
    <div class="abs" style="left:8px;top:368px;font-size:6.5px;color:#444;display:flex;align-items:center;gap:5px"><span style="width:9px;height:9px;border:1px solid #555"></span>Don't show it again</div>
  </div>
</section>

<section class="reviews">
  <h2 class="section-title reviews-title">Read the reviews</h2>
  <article class="review" style="left:128px"><div class="stars">★★★★★</div><h4>Mara Linden</h4><p>Lorem ipsum dolor sit amet, con se ctetur adipiscing elit, sed do eiusmod tempor incididunt ut labore et dolore magna aliqua. Quis ipsulores uspen disse ultrices gravida.</p></article>
  <article class="review" style="left:452px"><div class="stars">★★★★★</div><h4>Mara Linden</h4><p>Lorem ipsum dolor sit amet, con se ctetur adipiscing elit, sed do eiusmod tempor incididunt ut labore et dolore magna aliqua. Quis ipsulores uspen disse ultrices gravida.</p></article>
  <article class="review" style="left:774px"><div class="stars">★★★★★</div><h4>Mara Linden</h4><p>Lorem ipsum dolor sit amet, con se ctetur adipiscing elit, sed do eiusmod tempor incididunt ut labore et dolore magna aliqua. Quis ipsulores uspen disse ultrices gravida.</p></article>
  <div class="review-dots"><span></span><span></span><span></span><span></span><span></span></div>
</section>

<section class="cta">
  <div class="cta-art" role="img" aria-label="Illustration of a pile of wrapped gift boxes in red, green and gold"></div>
  <h2>Lorem ipsum dolor sit amesec tetur adipiscing eli sed do eiusmod.</h2>
  <div class="outline-btn">Contact Us</div>
</section>

<footer class="site-footer">
  <div class="label" style="left:131px;top:42px">Download our Velune app for a better experience !!</div>
  <div class="store" style="left:131px;top:76px"><i></i><div><small>GET IT ON</small><b>PlayHub</b></div></div>
  <div class="store" style="left:341px;top:76px"><i></i><div><small>Download on the</small><b>AppVault</b></div></div>
  <div class="label" style="left:851px;top:42px">Follow Us</div>
  <span class="social" style="left:763px;background:#3b5998" aria-label="Social link"></span>
  <span class="social" style="left:818px;background:#1da1f2" aria-label="Social link"></span>
  <span class="social" style="left:873px;background:linear-gradient(45deg,#f9a03f,#d6249f,#7b3fe4)" aria-label="Social link"></span>
  <span class="social" style="left:929px;background:#0a66c2" aria-label="Social link"></span>
  <span class="social" style="left:985px;background:#e62117" aria-label="Social link"></span>
  <div class="footer-rule"></div>
  <div class="copyright">Copyright © 2023 Velune. All rights reserved.</div>
</footer>

</body>
</html>
```